Velmora - Keystone Workplace Supply Services

Corporate style business card for directors of Franchisor.
VELMORA is a B2B Franchise.
Card should contain FRONT:
LOGO
NAME (Marcus Dellow)
TITLE (Director of Sales)
ADDRESS
Franchise Headquarters - 14 Pellick Ridge Road, Carrow Point, Qld, 4220. Australia
Phone: 1800 VELMORA - 1800 835 672
EMAIL - info@velmora-example.com.au
WEB - www.velmora-example.com.au

BACK: (Bullet points of services)
- Telecommunications
- Phone Systems & Plans
- Web Services
- IT Services
- Print Hardware & Rentals
- Consumable Supplies
- Maintenance & Support

Target Market(s)

Any Business Office environment

Industry/Entity Type

Business

Contact Information for Business Card

LOGO
NAME (Marcus Dellow)
TITLE (Director of Sales)
ADDRESS

- Telecommunications
- Phone Systems & Plans
- Web Services
- IT Services
- Consumable Supplies
- Maintenance & Support

Font styles to use
Sans Serif

Requirements
Must have
• Logo
• Corporate Style
Nice to have
• Keep with Logo base colours
Should not have
• Informal aspects

```html
<!DOCTYPE html>
<html lang="en">
<head>
<meta charset="utf-8">
<title>Velmora – Business Card</title>
<link rel="stylesheet" href="https://fonts.googleapis.com/css2?family=Arimo:wght@400;700&display=swap">
<style>
  :root {
    --orange: #e2561f;
    --ink: #151515;
    --grey-text: #3a3a3a;
    --card-white: #ffffff;
    --card-shade: #e4e4e4;
    --backdrop: #ececec;
  }
  * { box-sizing: border-box; margin: 0; padding: 0; }
  html, body {
    width: 1200px; height: 997px; overflow: hidden;
    background: var(--backdrop);
    font-family: "Arimo", Arial, sans-serif;
  }
  .card {
    position: absolute; width: 640px; height: 384px;
    background: radial-gradient(ellipse at 40% 35%, var(--card-white) 45%, var(--card-shade) 100%);
    box-shadow: 0 12px 30px rgba(0,0,0,.22);
    overflow: hidden;
  }
  .card-shape { position: absolute; inset: 0; }
  .card--back { left: 90px; top: 70px; }
  .card--front { left: 470px; top: 520px; }

  .wordmark {
    position: absolute; display: flex; align-items: center; gap: 12px;
    font-weight: 700; color: var(--ink); letter-spacing: 4px;
  }
  .wordmark-dot {
    border-radius: 50%; background: var(--orange); flex: none;
  }
  .card--back .wordmark { left: 70px; top: 110px; font-size: 46px; }
  .card--back .wordmark-dot { width: 34px; height: 34px; }
  .card--front .wordmark { left: 110px; top: 120px; font-size: 54px; }
  .card--front .wordmark-dot { width: 40px; height: 40px; }

  .services-heading {
    position: absolute; left: 300px; top: 192px;
    font-size: 15px; color: var(--grey-text);
    border-bottom: 2px solid var(--grey-text); padding-bottom: 2px;
  }
  .service-list { position: absolute; list-style: none; font-size: 15px; line-height: 24px; }
  .service-list li { display: flex; align-items: center; gap: 8px; color: var(--grey-text); }
  .service-list li.accent { color: var(--orange); }
  .service-list li::before, .service-list--right li::after {
    content: ""; width: 11px; height: 11px; border-radius: 50%;
    border: 2px solid var(--orange); flex: none;
  }
  .service-list--left { left: 40px; top: 270px; }
  .service-list--right { right: 30px; top: 36px; text-align: right; }
  .service-list--right li { justify-content: flex-end; }
  .service-list--right li::before { display: none; }

  .person { position: absolute; right: 38px; top: 198px; text-align: right; }
  .person-name { font-size: 20px; font-weight: 700; color: var(--orange); letter-spacing: .5px; }
  .person-title { font-size: 14px; font-weight: 700; color: var(--ink); margin-top: 2px; }

  .contact { position: absolute; left: 46px; top: 238px; font-size: 16px; font-weight: 700; color: var(--ink); }
  .contact-phone { margin-bottom: 30px; }
  .contact-line { line-height: 30px; }
  .icon-tab { position: absolute; left: 0; top: 254px; display: flex; flex-direction: column; gap: 11px; padding: 9px 0 0 7px; }
  .icon-tab svg { width: 16px; height: 16px; }
</style>
</head>
<body>

<section class="card card--back" aria-label="Card back – services">
  <svg class="card-shape" viewBox="0 0 640 384" aria-hidden="true">
    <path d="M0 0 H640 V4 H300 Q290 4 284 12 L280 18 H0 Z" fill="var(--orange)"/>
    <path d="M0 384 V378 H300 Q312 378 318 370 L324 362 H640 V384 Z" fill="var(--orange)"/>
  </svg>
  <div class="wordmark"><span>VELMORA</span><span class="wordmark-dot"></span></div>
  <div class="services-heading">Our Services</div>
  <ul class="service-list service-list--left">
    <li>Telecommunications</li>
    <li class="accent">Phone Systems &amp; Plans</li>
    <li>Web Services &amp; IT Services</li>
  </ul>
  <ul class="service-list service-list--right">
    <li class="accent">Print Hardware &amp; Rentals</li>
    <li>Consumable Supplies</li>
    <li class="accent">Maintenance &amp; Support</li>
  </ul>
</section>

<section class="card card--front" aria-label="Card front – contact">
  <svg class="card-shape" viewBox="0 0 640 384" aria-hidden="true">
    <path d="M0 0 H640 V16 H250 Q238 16 232 10 L226 4 H0 Z" fill="var(--orange)"/>
    <path d="M0 384 V364 H370 Q382 364 388 372 L392 378 H640 V384 Z" fill="var(--orange)"/>
    <rect x="-8" y="250" width="36" height="112" rx="8" fill="var(--ink)"/>
    <rect x="626" y="150" width="22" height="64" rx="6" fill="var(--ink)"/>
  </svg>
  <div class="wordmark"><span>VELMORA</span><span class="wordmark-dot"></span></div>
  <div class="person">
    <div class="person-name">MARCUS DELLOW</div>
    <div class="person-title">Director of Sales</div>
  </div>
  <div class="icon-tab" aria-hidden="true">
    <svg viewBox="0 0 16 16"><path d="M3 2 L6 2 L7 5 L5 6.5 Q6.5 9.5 9.5 11 L11 9 L14 10 L14 13 Q8 15 3 9 Q1 5 3 2 Z" fill="#fff"/></svg>
    <svg viewBox="0 0 16 16"><rect x="1.5" y="3.5" width="13" height="9" fill="none" stroke="#fff" stroke-width="1.5"/><path d="M1.5 3.5 L8 9 L14.5 3.5" fill="none" stroke="#fff" stroke-width="1.5"/></svg>
    <svg viewBox="0 0 16 16"><rect x="1.5" y="6" width="7" height="4" rx="2" transform="rotate(-45 5 8)" fill="none" stroke="#fff" stroke-width="1.5"/><rect x="7.5" y="6" width="7" height="4" rx="2" transform="rotate(-45 11 8)" fill="none" stroke="#fff" stroke-width="1.5"/></svg>
  </div>
  <div class="contact">
    <p class="contact-phone">1800 VELMORA - 1800 835 672</p>
    <p class="contact-line">info@velmora-example.com.au</p>
    <p class="contact-line">www.velmora-example.com.au</p>
  </div>
</section>

</body>
</html>
```